Magazine Ad for the Waste Industry

We need a full page ad design that will help us introduce our new engine cooling system into the Waste market. This system helps regulate engine temperatures for large trash trucks with its advanced technology and durable. We would like this ad to make an impact and stand out from the more cluttered looking ads that are seen in trade magazines.
The project must be submitted in either InDesign or Photoshop files.

Target Market(s)

Waste Industry, Trash truck manufacturers

Industry/Entity Type

Waste Management

Font styles to use
Sans Serif

Colors
0255a3

Requirements
Must have
• The text and images attached with a more modern industrial/masculine feel.
• Our Company colors are...
• Blue (RGB 25, 76, 159)
• Gray (RGB 129, 130, 133)
• White and black as accents as needed
• SIZING
• Spread Bleed: 9.5" x 11.375"
Nice to have
• I attached two files for a font that we have used in the past. Another font we use commonly is Ariel.

```html
<!DOCTYPE html>
<html lang="en">
<head>
<meta charset="utf-8">
<title>Advanced Electric Engine Cooling – Trade Ad</title>
<link rel="stylesheet" href="https://fonts.googleapis.com/css2?family=Exo+2:ital,wght@0,400;1,300;1,400;1,800;1,900&family=Roboto+Condensed:wght@700&display=swap">
<style>
  :root{
    --brand-blue:#1c4ca0;
    --deep-blue:#0255a3;
    --ink:#000000;
    --white:#ffffff;
    --gray:#818285;
    --ice:#d8eef8;
    --sky:#9fd6ef;
    --page:#f3f4f8;
  }
  html,body{margin:0;padding:0;width:1200px;height:1042px;overflow:hidden;background:var(--page);}
  .canvas{position:relative;width:1200px;height:1042px;overflow:hidden;}
  .ad{
    position:absolute;left:271px;top:141px;
    width:790px;height:945px;
    transform:scale(0.8);transform-origin:0 0;
    overflow:hidden;background:var(--white);
    font-family:"Exo 2",sans-serif;
  }
  .ad-backdrop{position:absolute;inset:0;width:790px;height:945px;}
  .headline{
    position:absolute;left:0;top:38px;width:790px;margin:0;
    text-align:center;color:var(--white);
    font-family:"Exo 2",sans-serif;font-style:italic;font-weight:900;
    font-size:58px;line-height:58px;letter-spacing:1px;text-transform:uppercase;
  }
  .product-visual{
    position:absolute;left:176px;top:188px;width:434px;height:434px;
    background:linear-gradient(135deg,#3a3d42 0%,#1b1c1f 55%,#2c2e33 100%);
    border-radius:6px;
  }
  .badge{
    position:absolute;left:531px;top:493px;width:222px;height:222px;
    border-radius:50%;background:var(--white);border:3px solid var(--brand-blue);
    box-sizing:border-box;display:flex;flex-direction:column;align-items:center;justify-content:center;gap:14px;
  }
  .badge-dot{width:70px;height:70px;border-radius:50%;background:var(--gray);}
  .badge-name{font-family:"Exo 2",sans-serif;font-weight:800;font-style:normal;font-size:34px;color:var(--brand-blue);letter-spacing:2px;}
  .benefits{position:absolute;left:44px;top:636px;margin:0;padding:0;list-style:none;}
  .benefits li{
    display:flex;align-items:center;gap:8px;height:38px;
    font-style:italic;font-weight:400;font-size:26px;color:var(--brand-blue);
  }
  .benefits .tick{width:26px;height:26px;flex:none;}
  .benefits .figure{color:var(--ink);}
  .contact-bar{position:absolute;left:0;top:864px;width:790px;height:81px;}
  .contact-phone{
    position:absolute;left:32px;top:872px;display:flex;align-items:center;gap:10px;
    color:var(--white);font-family:"Roboto Condensed",sans-serif;font-weight:700;font-size:50px;line-height:64px;
  }
  .contact-web{
    position:absolute;left:430px;top:893px;display:flex;align-items:center;gap:10px;
    color:var(--white);font-family:"Exo 2",sans-serif;font-style:italic;font-weight:800;font-size:20px;
  }
  .icon{flex:none;}
</style>
</head>
<body>
<div class="canvas">
  <section class="ad">
    <svg class="ad-backdrop" viewBox="0 0 790 945" aria-hidden="true">
      <defs>
        <linearGradient id="iceWash" x1="0" y1="0" x2="1" y2="1">
          <stop offset="0" stop-color="#cfeaf7"/>
          <stop offset="0.45" stop-color="#eef8fd"/>
          <stop offset="1" stop-color="#bfe3f4"/>
        </linearGradient>
      </defs>
      <rect width="790" height="945" fill="var(--white)"/>
      <rect y="180" width="790" height="700" fill="url(#iceWash)"/>
      <path d="M0 540 C220 420 520 300 790 140 L790 380 C560 520 300 640 0 760 Z" fill="var(--sky)" opacity="0.45"/>
      <path d="M0 790 C260 700 560 560 790 420 L790 520 C560 660 300 780 0 860 Z" fill="var(--white)" opacity="0.55"/>
      <path d="M0 540 C170 500 360 470 560 500 L560 520 C360 500 170 530 0 580 Z" fill="var(--ink)"/>
      <path d="M0 200 C300 300 560 220 790 120 L790 150 C560 250 300 320 0 215 Z" fill="var(--brand-blue)"/>
      <path d="M0 0 H790 V120 C560 220 300 290 0 200 Z" fill="var(--ink)"/>
      <path d="M0 864 H400 L434 945 H0 Z" fill="var(--brand-blue)"/>
      <path d="M400 879 H790 V945 H434 Z" fill="var(--ink)"/>
    </svg>

    <h1 class="headline">Advanced Electric<br>Engine Coolinga</h1>

    <div class="product-visual" role="img" aria-label="Electric engine cooling unit with four reversible fans"></div>

    <div class="badge">
      <span class="badge-dot"></span>
      <span class="badge-name">VOLTAIR</span>
    </div>

    <ul class="benefits">
      <li><svg class="tick" viewBox="0 0 26 26"><path d="M3 14 L10 22 L24 3" fill="none" stroke="var(--brand-blue)" stroke-width="3.5" stroke-linecap="round" stroke-linejoin="round"/></svg>Fully reversible fans</li>
      <li><svg class="tick" viewBox="0 0 26 26"><path d="M3 14 L10 22 L24 3" fill="none" stroke="var(--brand-blue)" stroke-width="3.5" stroke-linecap="round" stroke-linejoin="round"/></svg>Eliminate preventative maintenance</li>
      <li><svg class="tick" viewBox="0 0 26 26"><path d="M3 14 L10 22 L24 3" fill="none" stroke="var(--brand-blue)" stroke-width="3.5" stroke-linecap="round" stroke-linejoin="round"/></svg>Average&nbsp;<span class="figure">8%</span>&nbsp;fuel economy</li>
      <li><svg class="tick" viewBox="0 0 26 26"><path d="M3 14 L10 22 L24 3" fill="none" stroke="var(--brand-blue)" stroke-width="3.5" stroke-linecap="round" stroke-linejoin="round"/></svg>Increase Horsepower</li>
      <li><svg class="tick" viewBox="0 0 26 26"><path d="M3 14 L10 22 L24 3" fill="none" stroke="var(--brand-blue)" stroke-width="3.5" stroke-linecap="round" stroke-linejoin="round"/></svg>Quieter Residential Operation</li>
    </ul>

    <div class="contact-phone">
      <svg class="icon" width="40" height="40" viewBox="0 0 40 40" aria-hidden="true">
        <circle cx="20" cy="20" r="17" fill="none" stroke="var(--white)" stroke-width="2.5"/>
        <path d="M13 11 L17 11 L18.5 16 L16 18 C17 21 19 23 22 24 L24 21.5 L29 23 L29 27 C20 28 12 20 13 11 Z" fill="var(--white)"/>
      </svg>
      <span>(555) 214-0386</span>
    </div>

    <div class="contact-web">
      <svg class="icon" width="26" height="26" viewBox="0 0 26 26" aria-hidden="true">
        <circle cx="13" cy="13" r="11" fill="none" stroke="var(--white)" stroke-width="2"/>
        <ellipse cx="13" cy="13" rx="5" ry="11" fill="none" stroke="var(--white)" stroke-width="1.6"/>
        <path d="M2 13 H24 M4 7 H22 M4 19 H22" stroke="var(--white)" stroke-width="1.6"/>
      </svg>
      <span>www.northfan-systems.com/refuse</span>
    </div>
  </section>
</div>
</body>
</html>
```